Bref créative
Corvane Sales
Professional
Derek Vanholt
24915 Ashcombe Rd.
Elmridge, MI 48263-2975
dkvanholt@corvanesalesllc.example
www.corvanesalesllc.example
Font does not need to be the same as the logo font.
Logo and slogan
Delivering Dependable Solutions for the HVACR Trade

```html
<!DOCTYPE html>
<html lang="en">
<head>
<meta charset="utf-8">
<title>Corvane Sales — Business Card Set</title>
<link rel="stylesheet" href="https://fonts.googleapis.com/css2?family=Open+Sans:wght@300;400;700&display=swap">
<style>
  :root {
    --sheet: #dcdcdc;
    --card-white: #ffffff;
    --card-edge: #c4c4c4;
    --blue-light: #20b2ea;
    --blue-deep: #0a5fb4;
    --blue-name: #2aa6de;
    --red-swoosh: #e0261f;
    --orange: #f47a1f;
    --red-deep: #c8141c;
    --ink: #333333;
    --white: #ffffff;
    --mark-grey: #9a9a9a;
  }
  * { box-sizing: border-box; margin: 0; padding: 0; }
  html, body { width: 1200px; height: 725px; overflow: hidden; }
  body {
    background: var(--sheet);
    font-family: "Open Sans", Arial, sans-serif;
    position: relative;
  }
  .card {
    position: absolute;
    width: 571px;
    height: 329px;
    border: 1px solid var(--card-edge);
    overflow: hidden;
  }
  .card--front  { left: 22px;  top: 22px;  background: var(--card-white); }
  .card--blue   { left: 609px; top: 22px;  background: linear-gradient(135deg, var(--blue-light) 0%, var(--blue-deep) 100%); }
  .card--white  { left: 22px;  top: 374px; background: var(--card-white); }
  .card--orange { left: 609px; top: 374px; background: linear-gradient(90deg, var(--orange) 0%, var(--red-deep) 100%); }

  .header-band { position: absolute; left: 0; top: 0; width: 571px; height: 230px; }

  .contact {
    position: absolute;
    right: 22px;
    top: 18px;
    text-align: right;
    color: var(--white);
    font-size: 12px;
    line-height: 1.6;
  }

  .brand {
    display: flex;
    flex-direction: column;
    align-items: center;
    font-weight: 700;
    white-space: nowrap;
    line-height: 1;
  }
  .brand__dot { border-radius: 50%; flex: none; }

  .brand--small {
    position: absolute;
    left: 40px;
    top: 200px;
    gap: 14px;
    font-size: 26px;
    color: var(--red-swoosh);
  }
  .brand--small .brand__dot { width: 54px; height: 54px; background: var(--mark-grey); }

  .holder-name {
    position: absolute;
    right: 22px;
    top: 250px;
    font-size: 24px;
    font-weight: 300;
    line-height: 1.3;
    color: var(--blue-name);
  }

  .centered {
    position: absolute;
    left: 0;
    right: 0;
    top: 100px;
    display: flex;
    flex-direction: column;
    align-items: center;
  }
  .brand--large { gap: 20px; font-size: 38px; }
  .brand--large .brand__dot { width: 68px; height: 68px; }
  .tagline {
    margin-top: 28px;
    font-size: 15px;
    line-height: 1.65;
    text-align: center;
  }
  .on-color .brand, .on-color .tagline { color: var(--white); }
  .on-color .brand__dot { background: rgba(255,255,255,0.85); }
  .on-white .brand, .on-white .tagline { color: var(--ink); }
  .on-white .brand__dot { background: var(--mark-grey); }
</style>
</head>
<body>

  <section class="card card--front">
    <svg class="header-band" viewBox="0 0 571 230" aria-hidden="true">
      <defs>
        <linearGradient id="bandFill" x1="0" y1="0" x2="1" y2="1">
          <stop offset="0" stop-color="#1a7fd0"/>
          <stop offset="1" stop-color="#0a56a8"/>
        </linearGradient>
      </defs>
      <path d="M0 0 H571 V128 C470 150 380 130 280 150 C180 170 90 200 0 205 Z" fill="url(#bandFill)"/>
      <path d="M0 216 C90 210 180 182 280 162 C380 142 470 160 571 136 L571 128 C470 152 380 134 280 154 C180 174 90 204 0 210 Z" fill="var(--red-swoosh)"/>
    </svg>
    <div class="contact">
      <p>24915 Ashcombe Rd., Elmridge, MI 48263-2975</p>
      <p>Cell: (555) 010-0142 | Phone: (555) 010-0190 | Fax: (555) 010-0176</p>
      <p>Email: dkvanholt@corvanesalesllc.example | www.corvanesalesllc.example</p>
    </div>
    <div class="brand brand--small"><span class="brand__dot"></span>Corvane Sales</div>
    <p class="holder-name">Derek Vanholt</p>
  </section>

  <section class="card card--blue on-color">
    <div class="centered">
      <div class="brand brand--large"><span class="brand__dot"></span>Corvane Sales</div>
      <p class="tagline">Delivering Dependable Solutions<br>for the HVACR Trade</p>
    </div>
  </section>

  <section class="card card--white on-white">
    <div class="centered">
      <div class="brand brand--large"><span class="brand__dot"></span>Corvane Sales</div>
      <p class="tagline">Delivering Dependable Solutions<br>for the HVACR Trade</p>
    </div>
  </section>

  <section class="card card--orange on-color">
    <div class="centered">
      <div class="brand brand--large"><span class="brand__dot"></span>Corvane Sales</div>
      <p class="tagline">Delivering Dependable Solutions<br>for the HVACR Trade</p>
    </div>
  </section>

</body>
</html>
```